Brell Harbor Company Business Cards

Front and Back Business Card - logo and text setup - cool design. I need workable photoshop or illustrator files so I can setup each employee card with design that is created
Updates

Hi everyone, thank you for the great entries. Please no more white and blue cards - there are so many already - black and silver only now please. thanks!

Target Market(s)

Construction Industry - Facility Managers

Industry/Entity Type

Construction

Contact Information for Business Card

I really like contemporary simplistic looks - clean neat....not opposed to seeing some black backrounds

Requirements
Must have
• Logo/website address with design on front only - www.brellharbor-example.com (logo attached)
• Back:
• Name/Title/Company Address/Phone/email address
Nice to have
• Cool design
Should not have
• Nothing gimmicky like Fire or Water - since we are a Fire Protection company - it has all been done

```html
<!DOCTYPE html>
<html lang="en">
<head>
<meta charset="utf-8">
<title>Brell Harbor Company – Business Cards</title>
<link rel="stylesheet" href="https://fonts.googleapis.com/css2?family=PT+Sans:wght@400;700&display=swap">
<style>
  :root {
    --canvas-bg: #e6e6e8;
    --card-black: #141416;
    --card-silver: #c3c5ca;
    --mosaic-deep: #4a4b50;
    --mosaic-mid: #8a8c92;
    --text-silver: #c9cbd0;
    --shadow: rgba(0, 0, 0, 0.22);
  }
  * { box-sizing: border-box; margin: 0; padding: 0; }
  html, body {
    width: 1200px;
    height: 1200px;
    overflow: hidden;
    background: var(--canvas-bg);
    font-family: "PT Sans", sans-serif;
  }
  .sheet {
    width: 1200px;
    height: 1200px;
    display: flex;
    flex-direction: column;
    align-items: center;
    justify-content: center;
    gap: 60px;
  }
  .card {
    position: relative;
    width: 900px;
    height: 514px;
    overflow: hidden;
    box-shadow: 0 10px 28px var(--shadow);
  }
  .card-art {
    position: absolute;
    inset: 0;
    width: 100%;
    height: 100%;
  }
  .brand-name {
    position: absolute;
    left: 80px;
    top: 180px;
    font-weight: 700;
    font-size: 56px;
    line-height: 1;
    letter-spacing: -0.5px;
    color: var(--text-silver);
    display: flex;
    align-items: center;
    gap: 16px;
  }
  .brand-mark {
    width: 18px;
    height: 18px;
    background: var(--text-silver);
  }
  .website {
    position: absolute;
    left: 80px;
    top: 330px;
    font-size: 28px;
    color: var(--text-silver);
  }
  .contact-list {
    position: absolute;
    left: 560px;
    top: 150px;
    list-style: none;
    font-size: 36px;
    line-height: 1.22;
    color: var(--text-silver);
  }
</style>
</head>
<body>
<main class="sheet">

  <section class="card card-front" aria-label="Business card front">
    <svg class="card-art" viewBox="0 0 900 514">
      <defs>
        <linearGradient id="front-mosaic" x1="0" y1="0" x2="1" y2="0">
          <stop offset="0" stop-color="var(--card-black)"/>
          <stop offset="0.35" stop-color="var(--mosaic-deep)"/>
          <stop offset="0.7" stop-color="var(--mosaic-mid)"/>
          <stop offset="1" stop-color="var(--card-silver)"/>
        </linearGradient>
      </defs>
      <rect class="panel-black" width="900" height="514" fill="var(--card-black)"/>
      <polygon class="panel-silver" points="740,0 900,0 900,514 600,514" fill="var(--card-silver)"/>
      <polygon class="mosaic-band" role="img" aria-label="Diagonal band of square tiles"
               points="640,0 760,0 620,514 500,514" fill="url(#front-mosaic)"/>
    </svg>
    <div class="brand-name"><span>Brell Harbor</span><span class="brand-mark"></span></div>
    <p class="website">www.brellharbor-example.com</p>
  </section>

  <section class="card card-back" aria-label="Business card back">
    <svg class="card-art" viewBox="0 0 900 514">
      <defs>
        <linearGradient id="back-mosaic" x1="0" y1="0" x2="1" y2="0">
          <stop offset="0" stop-color="var(--card-silver)"/>
          <stop offset="0.3" stop-color="var(--mosaic-mid)"/>
          <stop offset="0.65" stop-color="var(--mosaic-deep)"/>
          <stop offset="1" stop-color="var(--card-black)"/>
        </linearGradient>
      </defs>
      <rect class="panel-black" width="900" height="514" fill="var(--card-black)"/>
      <polygon class="panel-silver" points="0,0 400,0 280,514 0,514" fill="var(--card-silver)"/>
      <polygon class="mosaic-band" role="img" aria-label="Diagonal band of square tiles"
               points="380,0 500,0 380,514 260,514" fill="url(#back-mosaic)"/>
    </svg>
    <ul class="contact-list">
      <li>name</li>
      <li>position</li>
      <li>company address</li>
      <li>phone</li>
      <li>E-mail address</li>
    </ul>
  </section>

</main>
</body>
</html>
```